Environmental Group Website Template

We want a website template for an environmental cause. The website should have a dark content area that is transparent. The website text and icons are white.
The background is a nature scene. The background image repeats.
Industry/Entity Type
Group

```html
<!DOCTYPE html>
<html lang="en">
<head>
<meta charset="utf-8">
<title>Greenwell Group</title>
<link rel="stylesheet" href="https://fonts.googleapis.com/css2?family=Roboto:wght@500;700&family=Lato:wght@400;700&display=swap">
<style>
:root{
  --sky-top:#a8b4f0;
  --sky-mid:#8a86c8;
  --water:#485590;
  --frame:rgba(30,32,52,.92);
  --panel:#23263a;
  --footer:#121522;
  --green:#4fa13a;
  --orange:#ea5a2a;
  --blue:#0d93dc;
  --yellow:#f3b833;
  --white:#ffffff;
  --muted:#dfe3ee;
}
*{box-sizing:border-box;margin:0;padding:0}
html,body{width:1003px;height:1200px;overflow:hidden}
body{
  position:relative;
  font-family:'Lato',sans-serif;
  color:var(--white);
  background:linear-gradient(180deg,var(--sky-top) 0%,var(--sky-mid) 20%,#6b5a86 26%,#2c3a2a 34%,#1f3140 44%,#3d4d88 58%,var(--water) 100%);
}
.scenery{position:absolute;inset:0}
.page{position:absolute;left:134px;top:13px;width:734px;height:1153px;background:var(--frame);border-radius:4px}
.header{position:absolute;left:144px;top:22px;width:714px;height:106px;background:var(--panel);border-radius:4px 4px 0 0}
.brand{position:absolute;left:157px;top:40px;display:flex;align-items:center;gap:10px}
.brand-dot{width:52px;height:52px;border-radius:50%;background:var(--green)}
.brand-name{font-family:'Lato',sans-serif;font-size:17px;line-height:20px;color:var(--white);font-weight:400;width:110px}
.search{position:absolute;left:672px;top:47px;width:174px;height:23px;background:var(--white);border-radius:2px;font-size:9px;color:#777;padding:6px 9px}
.search svg{position:absolute;right:6px;top:5px}
.nav{position:absolute;left:340px;top:97px;width:518px;height:31px;background:var(--green);clip-path:polygon(12px 0,100% 0,100% 100%,0 100%,8px 40%);display:flex;align-items:center;gap:0;padding-left:27px}
.nav a{font-family:'Roboto',sans-serif;font-weight:500;font-size:11.5px;color:var(--white);text-decoration:none;margin-right:25px}
.hero{position:absolute;left:144px;top:128px;width:714px;height:334px;border-radius:0 0 6px 6px;overflow:hidden;
  background:linear-gradient(90deg,#f8f8d8 0%,#eef0c0 38%,#e2c89a 55%,#c98a66 75%,#8a4a34 100%)}
.hero-copy{position:absolute;left:18px;top:28px;width:280px}
.hero h2{font-family:'Roboto',sans-serif;font-weight:500;font-size:19px;color:var(--orange);margin-bottom:8px}
.hero p{font-size:9.3px;line-height:16px;color:#222}
.btn{display:inline-block;border:2px solid var(--white);border-radius:2px;font-family:'Roboto',sans-serif;font-weight:700;font-size:8.5px;color:var(--white);padding:6px 7px;letter-spacing:.1px}
.hero .btn{border-color:var(--orange);color:var(--orange);background:#fff;margin-top:14px}
.dots{position:absolute;left:18px;top:306px;display:flex;gap:3px}
.dots span{width:9px;height:9px;border-radius:50%;background:#666}
.dots span:first-child{background:var(--green)}
.welcome{position:absolute;left:190px;top:488px;width:624px;text-align:center}
.welcome h1{font-family:'Roboto',sans-serif;font-weight:700;font-size:22px;margin-bottom:14px}
.welcome p{font-size:9.3px;line-height:16.3px;color:var(--muted)}
.welcome .btn{margin-top:24px}
.card{position:absolute;top:687px;width:202px;height:266px;border-radius:4px;text-align:center;padding-top:18px}
.card.blue{left:175px;background:var(--blue)}
.card.yellow{left:401px;background:var(--yellow)}
.card.green{left:626px;background:var(--green)}
.card-icon{width:70px;height:70px;margin:0 auto;border-radius:50%;background:rgba(255,255,255,.85)}
.card h3{font-family:'Roboto',sans-serif;font-weight:700;font-size:14px;line-height:16px;margin-top:17px}
.card p{font-size:9.3px;line-height:15.2px;margin:14px 18px 0}
.card .btn{margin-top:15px}
.footer{position:absolute;left:144px;top:984px;width:714px;height:172px;background:var(--footer);border-radius:4px}
.footer h4{position:absolute;top:30px;font-family:'Roboto',sans-serif;font-weight:700;font-size:13.5px}
.social{position:absolute;left:31px;top:56px;display:flex;gap:5px}
.social span{width:29px;height:29px;border-radius:50%;border:2px solid}
.contacts{position:absolute;left:322px;top:73px;display:flex;font-size:9px;line-height:14px}
.contact{display:flex;gap:7px;margin-right:14px}
.contact svg{flex:none}
.rule{position:absolute;left:31px;right:31px;top:113px;border-top:1px solid #262a3a}
.copy{position:absolute;left:0;right:0;top:130px;text-align:center;font-size:9.3px}
</style>
</head>
<body>
<div class="scenery" role="img" aria-label="Evening lakeside park with trees and city lights reflected in the water"></div>
<div class="page"></div>

<header class="header"></header>
<div class="brand"><span class="brand-dot"></span><span class="brand-name">Greenwell Group</span></div>
<div class="search">Search
  <svg width="11" height="11" viewBox="0 0 12 12"><circle cx="5" cy="5" r="3.8" fill="none" stroke="#4fa13a" stroke-width="1.8"/><line x1="8" y1="8" x2="11" y2="11" stroke="#4fa13a" stroke-width="1.8"/></svg>
</div>
<nav class="nav">
  <a href="#">HOME</a><a href="#">ABOUT</a><a href="#">EXPLORE</a><a href="#">CHALLENSES</a><a href="#">SOLUTIONS</a><a href="#">EVENTS</a><a href="#">NEWS</a>
</nav>

<section class="hero" role="img" aria-label="Photo of a woman drinking a glass of clean water">
  <div class="hero-copy">
    <h2>Lorem ipsum dolor sit amet</h2>
    <p>Lorem ipsum dolor sit amet, consectetuer adipiscing elit, sed diam nonummy nibh euismod tincidunt ut laoreet dolore magna aliquam erat volutpat. Ut wisi enim ...</p>
    <span class="btn">READ MORE</span>
  </div>
  <div class="dots"><span></span><span></span><span></span><span></span><span></span></div>
</section>

<section class="welcome">
  <h1>Welcome to Comapny Name</h1>
  <p>Lorem Ipsum is simply dummy text of the printing and typesetting industry. Lorem Ipsum has been the industry's standard dummy text ever since the 1500s, when an unknown printer took a galley of type and scrambled it to make a type specimen book. It has survived not only five centuries, but also the leap into electronic typesetting, remaining essentially unchanged. It was popularised in the 1960s with the release of Letraset sheets containing Lorem Ipsum passages, and more recently with desktop publishing software like Aldus PageMaker including versions of Lorem Ipsum.</p>
  <span class="btn">READ MORE</span>
</section>

<article class="card blue">
  <div class="card-icon" role="img" aria-label="Volunteer icon"></div>
  <h3>Volunteer<br>Volunteer Wmus</h3>
  <p>Lorem ipsum dolor sit amet, consectetuer adipiscing elit, sed diam laoreet dolore magna aliquam erat volutpat. Ut wisi enim ...</p>
  <span class="btn">READ MORE</span>
</article>
<article class="card yellow">
  <div class="card-icon" role="img" aria-label="Donate button icon"></div>
  <h3>Spport<br>Our Work</h3>
  <p>Lorem ipsum dolor sit amet, consectetuer adipiscing elit, sed diam laoreet dolore magna aliquam erat volutpat. Ut wisi enim ...</p>
  <span class="btn">READ MORE</span>
</article>
<article class="card green">
  <div class="card-icon" role="img" aria-label="Group with protest signs icon"></div>
  <h3>Make Your<br>Voice Heard</h3>
  <p>Lorem ipsum dolor sit amet, consectetuer adipiscing elit, sed diam laoreet dolore magna aliquam erat volutpat. Ut wisi enim ...</p>
  <span class="btn">READ MORE</span>
</article>

<footer class="footer">
  <h4 style="left:31px">Connect with us!</h4>
  <div class="social">
    <span style="border-color:#8a8f9e"></span>
    <span style="border-color:#3b5998"></span>
    <span style="border-color:#1da1f2"></span>
    <span style="border-color:#1a7bbf"></span>
    <span style="border-color:#d92c20"></span>
    <span style="border-color:#cf2030"></span>
    <span style="border-color:#f08a1c"></span>
  </div>
  <h4 style="left:322px">Get In Touch</h4>
  <div class="contacts">
    <div class="contact">
      <svg width="19" height="19" viewBox="0 0 20 20"><circle cx="10" cy="10" r="9" fill="none" stroke="#4fa13a" stroke-width="1.3"/><path d="M10 15c-2-3-3.2-4.6-3.2-6.2a3.2 3.2 0 0 1 6.4 0c0 1.6-1.2 3.2-3.2 6.2z" fill="#4fa13a"/></svg>
      <div>Your Company LTD.<br>Street Name, 000000,<br>City Name</div>
    </div>
    <div class="contact">
      <svg width="19" height="19" viewBox="0 0 20 20"><circle cx="10" cy="10" r="9" fill="none" stroke="#4fa13a" stroke-width="1.3"/><path d="M6.5 5.5l2 -.3 1 2.3-1.2 1a6 6 0 0 0 2.9 2.9l1-1.2 2.3 1-.3 2c-4.5.5-8.2-3.2-7.7-7.7z" fill="#4fa13a"/></svg>
      <div>Call Us<br>1-000-000-0000</div>
    </div>
    <div class="contact">
      <svg width="19" height="19" viewBox="0 0 20 20"><circle cx="10" cy="10" r="9" fill="none" stroke="#4fa13a" stroke-width="1.3"/><path d="M5.5 9l4.5-3 4.5 3v5h-9z M5.5 9l4.5 3 4.5-3" fill="none" stroke="#4fa13a" stroke-width="1.2"/></svg>
      <div>Email<br>info@greenwellgroup.org</div>
    </div>
  </div>
  <div class="rule"></div>
  <div class="copy">Copyright 2015 Company Name. All Rights Reserved</div>
</footer>
</body>
</html>
```